Organic Coconut oil

A label for a 500ml jar of organic coconut oil
The product is raw cold pressed virgin coconut oil
Target Market(s)
All health conscious individuals
Industry/Entity Type
Product
Requirements
Must have
- Virgin
Raw
Cold pressed
Organic
Product name tovi coconut oil

```html
<!DOCTYPE html>
<html lang="en">
<head>
<meta charset="utf-8">
<title>Tovi Virgin Coconut Oil – Jar Label</title>
<link href="https://fonts.googleapis.com/css2?family=Quicksand:wght@300;400;700&display=swap" rel="stylesheet">
<style>
  :root {
    --backdrop: #eeeeee;
    --label-white: #ffffff;
    --ring-grey: #d3d3d3;
    --brand-blue: #6cc1de;
    --ink: #2b2b2b;
    --ink-soft: #444444;
    --tone-husk: #a98462;
    --tone-flesh: #f3efe6;
    --tone-leaf: #7fae6c;
  }
  html, body {
    margin: 0;
    padding: 0;
    width: 1200px;
    height: 1200px;
    overflow: hidden;
    background: var(--backdrop);
  }
  .canvas {
    position: relative;
    width: 1200px;
    height: 1200px;
  }
  .label {
    position: absolute;
    left: 60px;
    top: 60px;
    width: 1080px;
    height: 1080px;
    border-radius: 50%;
    background: var(--label-white);
    box-shadow: 0 2px 10px rgba(0,0,0,0.08);
  }
  .label-ring {
    position: absolute;
    inset: 18px;
    border-radius: 50%;
    border: 22px solid var(--ring-grey);
  }
  .brand-name {
    position: absolute;
    top: 89px;
    left: 0;
    right: 0;
    margin: 0;
    text-align: center;
    font-family: "Quicksand", sans-serif;
    font-weight: 700;
    font-size: 260px;
    line-height: 1;
    letter-spacing: 10px;
    color: var(--brand-blue);
  }
  .product-name {
    position: absolute;
    top: 332px;
    left: 0;
    right: 0;
    margin: 0;
    text-align: center;
    font-family: "Quicksand", sans-serif;
    font-weight: 300;
    font-size: 108px;
    line-height: 1;
    color: var(--ink);
  }
  .coconut-visual {
    position: absolute;
    left: 120px;
    top: 500px;
    width: 800px;
    height: 390px;
    border-radius: 24px;
    background: linear-gradient(135deg, var(--tone-flesh) 0%, var(--tone-husk) 60%, var(--tone-leaf) 100%);
  }
  .claims {
    position: absolute;
    top: 920px;
    left: 0;
    right: 0;
    margin: 0;
    text-align: center;
    font-family: "Quicksand", sans-serif;
    font-weight: 400;
    font-size: 34px;
    line-height: 1.2;
    color: var(--ink-soft);
  }
  .net-weight {
    position: absolute;
    top: 982px;
    left: 0;
    right: 0;
    margin: 0;
    text-align: center;
    font-family: "Quicksand", sans-serif;
    font-weight: 400;
    font-size: 38px;
    line-height: 1.2;
    color: var(--ink-soft);
  }
</style>
</head>
<body>
  <main class="canvas">
    <section class="label">
      <div class="label-ring"></div>
      <h1 class="brand-name">TOVI</h1>
      <p class="product-name">virgin coconut oil</p>
      <div class="coconut-visual" role="img" aria-label="Photograph of a whole coconut and two halved coconuts with white flesh resting on green palm leaves"></div>
      <p class="claims">100% Organic Raw Cold Pressed</p>
      <p class="net-weight">500g</p>
    </section>
  </main>
</body>
</html>
```